LR Quick Quote Screen

We are looking for two things:
1. On our main website (www.lindellridge-example.com) we would like to add a section for someone to enter their address and email address in return for a "quick quote."
2. Once they hit "enter" we would like a page built out that contains all the information that we would plug in from the backend.
We are an insurance company that focuses on property and powersports. This project in particular would focus on property (homeowner's specifically).
Reason: One of the decision makers will be out of the office until next week so we will provide our response next Tuesday. Thank you for your patience!
Insurance

```html
<!DOCTYPE html>
<html lang="en">
<head>
<meta charset="utf-8">
<title>Lindell Ridge Insurance Company</title>
<link rel="stylesheet" href="https://fonts.googleapis.com/css2?family=PT+Serif:wght@400;700&family=Noto+Sans:wght@400;700&family=Fira+Sans:wght@400;500;600&display=swap">
<style>
:root{
  --navy:#1c2f6b;
  --red:#c21a1a;
  --grey-text:#8a8a8a;
  --panel:#e2ded6;
  --bar-top:#9a9494;
  --bar-bottom:#5f5858;
  --blue:#1a63b8;
  --blue-light:#3fa0e6;
  --green:#2f7a16;
  --orange:#e29a0e;
  --link:#1a5fb0;
  --footer-top:#19b3e6;
  --footer-bottom:#1f62b8;
  --ink:#111;
}
*{box-sizing:border-box;margin:0;padding:0}
html,body{width:759px;height:1200px;overflow:hidden;background:#fff}
body{position:relative;font-family:"Noto Sans",sans-serif;color:var(--ink)}
.abs{position:absolute}

/* header */
.brand{left:14px;top:22px;display:flex;align-items:center;gap:8px}
.brand-dot{width:14px;height:14px;border-radius:50%;background:var(--navy)}
.brand-name{font-family:"PT Serif",serif;font-size:25px;color:var(--navy);line-height:1}
.brand-sub{left:36px;top:56px;font-family:"PT Serif",serif;font-size:9px;letter-spacing:2px;color:var(--navy)}
.util-icons{left:502px;top:57px;display:flex;gap:12px}
.search{left:582px;top:55px;width:140px;height:19px;border:1px solid #222;font-size:10px;padding:2px 5px}
.search-icon{left:731px;top:58px}

/* hero */
.hero{left:0;top:93px;width:552px;height:206px;border:2px solid #d9d9d9;background:linear-gradient(90deg,#f4f4f4,#e6e6e6 60%,#f0f0f0);overflow:hidden}
.hero-lock{left:26px;top:75px;width:96px;height:106px;border-radius:10px;background:linear-gradient(#d8d8d8,#8f8f8f)}
.hero-person{left:224px;top:-2px;width:232px;height:208px;background:linear-gradient(160deg,#c8925f,#e9c4a6 45%,#c8211b 75%)}
.hero-have{left:134px;top:52px;font-family:"PT Serif",serif;font-size:38px;color:var(--red);line-height:1}
.hero-future{left:172px;top:83px;font-family:"PT Serif",serif;font-size:24px;color:#555}
.hero-protected{left:133px;top:104px;font-family:"PT Serif",serif;font-size:28px;color:#a6a6a6;letter-spacing:1px}
.more{display:flex;align-items:center;gap:6px;font-family:"PT Serif",serif;font-size:15px}
.hero .more{left:138px;top:161px;color:var(--red)}
.more svg{flex:none}

/* nav */
.nav{left:555px;top:93px;width:204px}
.nav a{display:block;position:relative;height:41px;margin-bottom:0.5px;border-radius:20px 0 0 20px;background:linear-gradient(#f0eeea,#d6d2cc);font-family:"PT Serif",serif;font-size:14px;color:#8a8580;text-decoration:none;padding:11px 13px}
.nav a::after{content:"";position:absolute;right:12px;top:13px;width:14px;height:14px;border-radius:50%;background:#fff;box-shadow:inset 0 0 0 2px #bdb8b1}
.nav a.active{background:linear-gradient(#2f8ce0,#0f4f9e);color:#fff}
.nav a.active::after{box-shadow:inset 0 0 0 2px #fff}

/* section bars */
.bar{height:41px;background:linear-gradient(var(--bar-top),var(--bar-bottom));font-family:"PT Serif",serif;font-weight:700;font-size:17px;color:#fff;padding:10px 21px}

.about-text{left:0;top:347px;width:552px;height:90px;background:var(--panel);font-size:8.6px;line-height:16px;padding:11px 10px}

/* cards */
.cards{left:0;top:437px;width:552px;display:flex;gap:2px}
.card{width:182.6px;height:203px;background:var(--panel)}
.card-img{position:relative;height:106px}
.card-label{position:absolute;left:0;bottom:0;width:100%;height:29px;background:rgba(0,0,0,.45);color:#fff;font-family:"Fira Sans",sans-serif;font-size:15px;display:flex;align-items:center;gap:6px;padding-left:10px}
.card h3{font-size:9.5px;font-weight:700;margin:10px 9px 3px}
.card p{font-size:8.5px;line-height:10.5px;text-decoration:underline;margin:0 9px}
.card .more{margin:14px 0 0 15px;color:#333}

/* eDelivery */
.edelivery{left:13px;top:700px;width:520px;font-size:9.3px;line-height:16px}
.edelivery p{margin-bottom:15px}
.edelivery span{color:var(--link)}
.starburst{left:403px;top:816px}

/* policy holders */
.pill{left:569px;width:164px;height:38px;border-radius:19px;border:1px solid #222;color:#fff;font-family:"Fira Sans",sans-serif;font-weight:500;font-size:16px;letter-spacing:.5px;display:flex;align-items:center;justify-content:center}
.pill.login{top:360px;background:linear-gradient(#4cb0ef,#1665b8)}
.pill.pay{top:413px;background:linear-gradient(#4e9a2a,#24650d)}
.pill.claim{top:474px;background:linear-gradient(#f5bd34,#d8880a)}
.note{left:569px;width:164px;text-align:center;font-size:8.5px;font-weight:700}

.hatch{left:555px;top:543px;width:204px;height:6px;background:repeating-linear-gradient(135deg,#bbb 0 2px,#fff 2px 4px)}
.quote{left:555px;top:592px;width:204px;height:358px;background:var(--panel);padding:15px 17px}
.quote label{display:block;font-size:11.5px;font-weight:700;margin-bottom:5px}
.quote .field{width:166px;height:25px;border:1px solid #222;background:#fff;margin-bottom:14px}
.quote .field.area{height:83px}
.submit{left:639px;top:915px;width:94px;height:22px;border-radius:11px;border:1px solid #222;background:linear-gradient(#4cb0ef,#1665b8);color:#fff;font-family:"Fira Sans",sans-serif;font-size:12px;font-weight:600;text-align:center;line-height:20px}

/* footer */
.footer{left:0;top:958px;width:759px;height:217px;background:linear-gradient(var(--footer-top),var(--footer-bottom));color:#fff;font-family:"Fira Sans",sans-serif}
.footer h4{position:absolute;font-size:14px;font-weight:600}
.footer ul{position:absolute;list-style:none;font-size:12px;line-height:20.6px}
.footer .rule{position:absolute;height:1px;background:rgba(255,255,255,.35)}
.badge{left:574px;top:30px;width:94px;height:34px;border-radius:50%;background:linear-gradient(#f3f3f3,#9aa4b4);border:2px solid #d6dbe4}
.rating{left:520px;top:75px;width:200px;text-align:center;font-size:11px;line-height:15px}
.social{display:flex;align-items:center;gap:8px;font-size:13px;font-weight:500}
.social i{display:block;width:24px;height:24px;border-radius:3px;background:#fff}

.bottom{left:0;top:1175px;width:759px;height:25px;font-size:10px;font-weight:700;color:#333}
.bottom .copy{position:absolute;left:9px;top:7px}
.bottom .links{position:absolute;left:416px;top:7px;word-spacing:2px}
</style>
</head>
<body>

<header>
  <div class="abs brand"><span class="brand-dot"></span><span class="brand-name">Lindell Ridge</span></div>
  <div class="abs brand-sub">INSURANCE COMPANY</div>
  <div class="abs util-icons">
    <svg width="11" height="11" viewBox="0 0 11 11"><path d="M1 6 5.5 1.5 10 6M2.5 5v5h6V5" fill="none" stroke="#222"/></svg>
    <svg width="11" height="11" viewBox="0 0 11 11"><path d="M5.5 0v11M0 5.5h11M3.5 2 5.5 0 7.5 2M3.5 9l2 2 2-2M2 3.5 0 5.5l2 2M9 3.5l2 2-2 2" fill="none" stroke="#222"/></svg>
    <svg width="12" height="10" viewBox="0 0 12 10"><rect x=".5" y=".5" width="11" height="9" fill="none" stroke="#222"/><path d="M.5.5 6 5l5.5-4.5" fill="none" stroke="#222"/></svg>
  </div>
  <div class="abs search">enter keyword</div>
  <svg class="abs search-icon" width="12" height="12" viewBox="0 0 12 12"><circle cx="4.5" cy="4.5" r="3.5" fill="none" stroke="#222" stroke-width="1.5"/><path d="M7 7l4 4" stroke="#222" stroke-width="2"/></svg>
</header>

<section class="abs hero">
  <div class="abs hero-lock" role="img" aria-label="Padlock with a red check mark"></div>
  <div class="abs hero-person" role="img" aria-label="Smiling woman in a red sweater adjusting her glasses"></div>
  <div class="abs hero-have">Have</div>
  <div class="abs hero-future">your future</div>
  <div class="abs hero-protected">PROTECTED</div>
  <div class="abs more"><svg width="14" height="14" viewBox="0 0 14 14"><circle cx="7" cy="7" r="6" fill="none" stroke="#222" stroke-width="1.5"/><path d="M5.5 4v6l4.5-3z" fill="#222"/></svg>MORE</div>
</section>

<nav class="abs nav">
  <a href="#">Home</a>
  <a href="#">About Us</a>
  <a href="#" class="active">Producer Locator</a>
  <a href="#">Producer Login</a>
  <a href="#">Our Products</a>
</nav>

<h2 class="abs bar" style="left:0;top:302px;width:552px">About Us</h2>
<div class="abs about-text">Lindell Ridge Insurance Company (LRIC) - The flagship of the Harwell Group of Affiliated Companies is recognized as an industry leader in motorcycle and personal watercraft coverage. LRIC also offers automotive, homeowners, dwelling fire, boat, motor home, mobile home and commercial products, and has become the "one spot" independent brokers and agents can source all their clients' coverage needs</div>

<div class="abs cards">
  <article class="card">
    <div class="card-img" role="img" aria-label="Mother and child laughing together" style="background:linear-gradient(135deg,#c97a55,#f0c7b0 50%,#d98aa6)">
      <div class="card-label"><svg width="12" height="12" viewBox="0 0 12 12"><circle cx="6" cy="6" r="5.3" fill="none" stroke="#fff" stroke-width="1.3"/><path d="M4.7 3.5v5l4-2.5z" fill="#fff"/></svg>LIFE Insurance</div>
    </div>
    <h3>Nunc suscipit</h3>
    <p>Suspendisse enim arcu, convallis non, cursus sed, dignissim et, est. Aenean semper aliquet libero.</p>
    <div class="more"><svg width="14" height="14" viewBox="0 0 14 14"><circle cx="7" cy="7" r="6" fill="none" stroke="#222" stroke-width="1.5"/><path d="M5.5 4v6l4.5-3z" fill="#222"/></svg>MORE</div>
  </article>
  <article class="card">
    <div class="card-img" role="img" aria-label="Silver convertible on a country road" style="background:linear-gradient(#b9cde0,#dfe3e6 40%,#9aa2a8 70%,#6f8a54)">
      <div class="card-label"><svg width="12" height="12" viewBox="0 0 12 12"><circle cx="6" cy="6" r="5.3" fill="none" stroke="#fff" stroke-width="1.3"/><path d="M4.7 3.5v5l4-2.5z" fill="#fff"/></svg>AUTO Insurance</div>
    </div>
    <h3>Lorem ipsum dolo</h3>
    <p>In ante velit, cursus ut, ultrices vitae, tempor ut, risus. Duis pulvinar. Vestibulum vel pede at sapien</p>
    <div class="more"><svg width="14" height="14" viewBox="0 0 14 14"><circle cx="7" cy="7" r="6" fill="none" stroke="#222" stroke-width="1.5"/><path d="M5.5 4v6l4.5-3z" fill="#222"/></svg>MORE</div>
  </article>
  <article class="card" style="background:#eeebe6">
    <div class="card-img" role="img" aria-label="Two-storey house with a red tile roof" style="background:linear-gradient(#8fb8e0,#c9d3d8 40%,#b86a4e 65%,#6f8f4a)">
      <div class="card-label"><svg width="12" height="12" viewBox="0 0 12 12"><circle cx="6" cy="6" r="5.3" fill="none" stroke="#fff" stroke-width="1.3"/><path d="M4.7 3.5v5l4-2.5z" fill="#fff"/></svg>HOME Insurance</div>
    </div>
    <h3>Aenean semper</h3>
    <p>Suspendisse enim arcu, convallis non, cursus sed, dignissim et, est. Aenean semper aliquet libero.</p>
    <div class="more"><svg width="14" height="14" viewBox="0 0 14 14"><circle cx="7" cy="7" r="6" fill="none" stroke="#222" stroke-width="1.5"/><path d="M5.5 4v6l4.5-3z" fill="#222"/></svg>MORE</div>
  </article>
</div>

<h2 class="abs bar" style="left:0;top:645px;width:552px">eDelivery</h2>
<div class="abs edelivery">
  <p>We are pleased to announce that our new e-delivery policy service is now available. Instead of receiving paper copies of policy documents, you now have the option of accessing your policy documents online at any time.</p>
  <p><span>Convenient</span> - Whether working, traveling or at home, your most recent policy documents will always be available online from any computer with an internet connection.</p>
  <p><span>Safe and secure</span> - Rest assured knowing your policy account information is secure in your own<br>online password protected account.</p>
  <p><span>Help the environment</span> - Having policy documents delivered electronically<br>not only saves time - it saves trees!</p>
  <p>Enrolling is easy! Simply login above (or register if you have not done so<br>already) and select the Paperless Options under My Account.</p>
</div>
<svg class="abs starburst" width="126" height="124" viewBox="0 0 126 124">
  <defs><radialGradient id="burst" cx="45%" cy="40%" r="60%"><stop offset="0" stop-color="#7fd24a"/><stop offset="1" stop-color="#1f7a12"/></radialGradient></defs>
  <polygon fill="url(#burst)" points="63,2 72,18 88,8 91,27 110,24 105,42 123,50 108,62 121,77 102,81 105,100 86,96 80,115 67,102 55,120 47,101 29,111 28,92 9,91 17,74 2,64 17,53 6,37 25,34 22,15 40,21 47,3 55,19"/>
  <g transform="rotate(-20 63 62)" fill="#fff" font-family="Fira Sans, sans-serif" font-weight="600" text-anchor="middle">
    <text x="63" y="50" font-size="15">Sign Up</text>
    <text x="63" y="67" font-size="15">for</text>
    <text x="63" y="84" font-size="15">eDelivery</text>
  </g>
</svg>

<h2 class="abs bar" style="left:555px;top:302px;width:204px">Policy Holders</h2>
<div class="abs pill login">Customer Login</div>
<div class="abs pill pay">Make Payment</div>
<div class="abs note" style="top:455px">Login not required</div>
<div class="abs pill claim">Report a Claim</div>
<div class="abs note" style="top:516px">Login not required</div>

<div class="abs hatch"></div>
<h2 class="abs bar" style="left:555px;top:549px;width:204px">Quick Quote</h2>
<form class="abs quote">
  <label>Name</label><div class="field"></div>
  <label>E-Mail</label><div class="field"></div>
  <label>Phone</label><div class="field" style="margin-bottom:18px"></div>
  <label>Address</label><div class="field area"></div>
</form>
<div class="abs submit">Submit</div>

<footer class="abs footer">
  <h4 style="left:37px;top:19px">Product Quick Links</h4>
  <div class="rule" style="left:37px;top:43px;width:427px"></div>
  <h4 style="left:37px;top:52px">Property</h4>
  <ul style="left:45px;top:80px"><li>Homeowners</li><li>Renters</li><li>Condominium</li><li>Manufactured Home</li></ul>
  <h4 style="left:218px;top:52px">Powersports</h4>
  <ul style="left:227px;top:80px"><li>Motorcycle</li><li>Off-Road/ATV</li><li>Personal Watercraft</li><li>Pleasure Boat</li><li>Motorhome</li><li>Travel Trailer</li></ul>
  <h4 style="left:389px;top:52px">Liability</h4>
  <ul style="left:400px;top:80px"><li>Umbrella</li></ul>
  <div class="rule" style="left:488px;top:36px;width:1px;height:170px"></div>
  <div class="abs badge" role="img" aria-label="Financial strength rating badge"></div>
  <div class="abs rating">Keystone Rating of A<br>for financial strength and stability.</div>
  <h4 style="left:520px;top:132px">Staty Connected</h4>
  <div class="rule" style="left:520px;top:156px;width:210px"></div>
  <div class="abs social" style="left:522px;top:170px"><i></i>Newsfeed</div>
  <div class="abs social" style="left:628px;top:170px"><i></i>Chirper</div>
</footer>

<div class="abs bottom">
  <span class="copy">Copyrights Reserverd @ 2012</span>
  <span class="links">Careers &nbsp;| &nbsp;Privacy Policy &nbsp;| &nbsp;Contact Us &nbsp;| &nbsp;Nota a producer</span>
</div>

</body>
</html>
```